Poster for Office

Looking for an edgy, beautiful poster to hang up in my office that uses the quotes located below and potentially the image attached.

Title: Hadley's Maxims

Must have the following quotes included (punctuation and capitalization are flexible, do what you think looks the best they also don't need the quotation symbols):

"Don't order fish at a steakhouse"
"Be bold. The more you tell, the more you sell"
"admit nothing, deny everything, launch counterattack."
"avoid obviousness"
"never do anything until you're ready to do it"
"look good=feel good"
"always keep the advantage"
"never complain, never explain"
"Lay low, play dumb, keep moving"

Quotes

• Title: Hadley's Maxims

"avoid obviousness"
"look good=feel good"

```html
<!DOCTYPE html>
<html lang="en">
<head>
<meta charset="utf-8">
<title>Hadley's Maxims</title>
<link rel="stylesheet" href="https://fonts.googleapis.com/css2?family=Black+Ops+One&family=Jura:wght@500&display=swap">
<style>
  :root {
    --water-top: #c9b39a;
    --water-haze: #8fa095;
    --water-mid: #4e6a63;
    --water-deep: #2a3a38;
    --water-floor: #1c2626;
    --title-fill: #5f6e5e;
    --title-edge: #2b3430;
    --quote-ink: #f4f2ec;
    --frame-line: rgba(20, 26, 24, 0.85);
    --frame-tint: rgba(18, 28, 27, 0.18);
  }
  html, body {
    margin: 0;
    padding: 0;
    width: 849px;
    height: 1200px;
    overflow: hidden;
    background: var(--water-floor);
  }
  .poster {
    position: relative;
    width: 849px;
    height: 1200px;
    overflow: hidden;
  }
  .poster__backdrop {
    position: absolute;
    inset: 0;
    background:
      radial-gradient(ellipse 60% 40% at 62% 30%, rgba(214, 190, 160, 0.35), transparent 70%),
      linear-gradient(180deg,
        var(--water-top) 0%,
        var(--water-haze) 14%,
        var(--water-mid) 34%,
        var(--water-deep) 62%,
        var(--water-floor) 100%);
  }
  .poster__title {
    position: absolute;
    left: 38px;
    top: 168px;
    margin: 0;
    font-family: "Black Ops One", system-ui, sans-serif;
    font-weight: 400;
    font-size: 58px;
    letter-spacing: 1px;
    line-height: 1;
    text-transform: uppercase;
    color: var(--title-fill);
    -webkit-text-stroke: 2px var(--title-edge);
    text-shadow: 2px 2px 0 var(--title-edge);
  }
  .maxims {
    position: absolute;
    left: 36px;
    top: 325px;
    width: 792px;
    height: 677px;
    box-sizing: border-box;
    border: 1px dashed var(--frame-line);
    background: var(--frame-tint);
    margin: 0;
    padding: 20px 0 0 4px;
    list-style: none;
  }
  .maxims__item {
    font-family: "Jura", sans-serif;
    font-weight: 500;
    font-size: 28.5px;
    line-height: 72.6px;
    letter-spacing: 0.6px;
    color: var(--quote-ink);
    white-space: nowrap;
  }
</style>
</head>
<body>
  <main class="poster">
    <div class="poster__backdrop" role="img" aria-label="Photograph of smooth stepping stones crossing calm water at sunset"></div>
    <h1 class="poster__title">Hadley's Maxims</h1>
    <ul class="maxims">
      <li class="maxims__item">"Don't order fish at a steakhouse"</li>
      <li class="maxims__item">"Be bold. The more you tell, the more you sell"</li>
      <li class="maxims__item">"Admit nothing, deny everything, launch counterattack."</li>
      <li class="maxims__item">"Avoid obviousness"</li>
      <li class="maxims__item">"Never do anything until you're ready to do it"</li>
      <li class="maxims__item">"Look good=feel good"</li>
      <li class="maxims__item">"Always keep the advantage"</li>
      <li class="maxims__item">"Never complain, never explain"</li>
      <li class="maxims__item">"Lay low, play dumb, keep moving"</li>
    </ul>
  </main>
</body>
</html>
```